Business Card Design Project

Basic business card with minimal details. I just need company name, email & web address, telephone and my name.
I would like the back of the card to be grey with my logo & company name centred.

Target Market(s)

Architects
Builders
Property Developers

Industry/Entity Type

Business

Font styles to use
Sans Serif

Colors

Designer to choose colors to be used in the design.

Requirements
Must have
• Framewise Build
Marcus Helby - Director
M: 0427 593184
E: marcus@framewisebuild.com.au
W: www.framewisebuild.com.au
Should not have
• No other images or pictures

```html
<!DOCTYPE html>
<html lang="en">
<head>
<meta charset="utf-8">
<title>Framewise Build — Business Card</title>
<link href="https://fonts.googleapis.com/css2?family=Open+Sans:wght@400;600;700&display=swap" rel="stylesheet">
<style>
  :root {
    --backdrop: #ececec;
    --card-white: #f7f7f7;
    --slate: #566570;
    --ink: #5d656b;
    --crimson: #b5123f;
    --paper-line: #ffffff;
  }
  * { box-sizing: border-box; margin: 0; padding: 0; }
  html, body {
    width: 1200px;
    height: 900px;
    overflow: hidden;
    background: var(--backdrop);
    font-family: "Open Sans", Arial, sans-serif;
  }
  .sheet {
    width: 1200px;
    height: 900px;
    display: flex;
    flex-direction: column;
    align-items: center;
    justify-content: center;
    gap: 40px;
  }
  .card {
    position: relative;
    width: 700px;
    height: 400px;
    box-shadow: 0 4px 14px rgba(0,0,0,0.12);
  }
  .card-front { background: var(--card-white); color: var(--ink); }
  .card-back {
    background: var(--slate);
    display: flex;
    align-items: center;
    justify-content: center;
  }

  .brand {
    display: flex;
    align-items: center;
    gap: 18px;
  }
  .brand-mark {
    width: 34px;
    height: 34px;
    background: var(--crimson);
  }
  .brand-name {
    font-weight: 400;
    font-size: 36px;
    letter-spacing: 5px;
    text-transform: uppercase;
    color: var(--ink);
  }
  .card-front .brand {
    position: absolute;
    top: 52px;
    left: 52px;
  }
  .card-back .brand-mark { background: var(--paper-line); width: 40px; height: 40px; }
  .card-back .brand-name { color: var(--paper-line); font-size: 38px; }

  .contact {
    position: absolute;
    left: 52px;
    top: 150px;
    font-size: 17px;
    line-height: 1.45;
  }
  .contact-name {
    font-weight: 700;
    font-size: 22px;
    color: var(--crimson);
  }
  .contact-role {
    font-weight: 600;
    font-size: 16px;
    margin-bottom: 14px;
  }
  .contact-line .label {
    display: inline-block;
    width: 24px;
    color: var(--crimson);
    font-weight: 600;
  }

  .address {
    position: absolute;
    right: 52px;
    bottom: 48px;
    font-size: 16px;
    line-height: 1.4;
  }
  .address-company {
    color: var(--crimson);
    text-transform: uppercase;
    letter-spacing: 0.5px;
  }
</style>
</head>
<body>
<main class="sheet">
  <section class="card card-front" aria-label="Business card front">
    <div class="brand">
      <span class="brand-mark"></span>
      <span class="brand-name">Framewise Build</span>
    </div>
    <div class="contact">
      <p class="contact-name">Marcus Helby</p>
      <p class="contact-role">Director</p>
      <p class="contact-line"><span class="label">M</span>0427 593184</p>
      <p class="contact-line"><span class="label">E</span>marcus@framewisebuild.com.au</p>
      <p class="contact-line"><span class="label">W</span>www.framewisebuild.com.au</p>
    </div>
    <address class="address" style="font-style:normal">
      <p class="address-company">Framewise Build</p>
      <p>48 Harlow St</p>
      <p>Fairfield North</p>
    </address>
  </section>

  <section class="card card-back" aria-label="Business card back">
    <div class="brand">
      <span class="brand-mark"></span>
      <span class="brand-name">Framewise Build</span>
    </div>
  </section>
</main>
</body>
</html>
```